Investment firm needs refreshed corporate powerpoint slides design

We need a new and refreshed powerpoint template for our corporate investment deck. We are a technology private equity group that primarily invests in fast growing software companies and we would like to reflect that in a modern and light blue / transparant / white powerpoint and fonts template. I have also attached our old investor deck as a guideline and also check out our website to get an idea of what we do and what type of companies we invested in. Please note that our website is old and so our presentation should be a refreshed "2017" modern design, not a copy / paste of our website design and graphics.
Updates

Target Market(s)

Investors such as high net worth individuals, pension funds, banks, financial advisors

Industry/Entity Type

Investment

Colors
33a6d7
85cae6
cfeae6
edf8f6
ffffff
fff3d1
86cfc6

Requirements
Must have
• We let you be creative, we trust you have seen more investment presentations before.
Nice to have
• Pre-built models, flow charts, graphs, charts, etc.
Should not have
• Fancy or edgy images, this has to be a modern, fresh and trustworthy looking powerpoint template. No stock images, if you do use stock images for background purposes please be creative! :-)

```html
<!DOCTYPE html>
<html lang="en">
<head>
<meta charset="utf-8">
<title>Slide template overview – part 1</title>
<link href="https://fonts.googleapis.com/css2?family=Open+Sans:wght@400;600;700&family=Roboto+Condensed:wght@400;700&display=swap" rel="stylesheet">
<style>
:root{
  --stage:#1c3c3a;
  --board:#c9ccd0;
  --title-ink:#7fa7a2;
  --blue:#33a6d7;
  --deep:#2f86c9;
  --teal:#2cc0cf;
  --sky:#85cae6;
  --mint:#cfeae6;
  --pale:#edf8f6;
  --cream:#fff3d1;
  --sea:#86cfc6;
  --navy:#1f4f78;
  --ink:#3a3a3a;
  --soft:#8a8a8a;
  --green:#8cc63f;
  --gold:#f5b820;
  --dark:#0f2a55;
}
*{box-sizing:border-box;margin:0;padding:0}
html,body{width:1200px;height:1200px;overflow:hidden;background:var(--stage);font-family:'Open Sans',sans-serif;color:var(--ink)}
.page-title{position:absolute;top:24px;left:0;width:1200px;text-align:center;font:400 19px 'Open Sans',sans-serif;letter-spacing:1.5px;color:var(--title-ink)}
.board{position:absolute;left:18px;top:77px;width:1160px;height:1016px;background:var(--board)}
.slide{position:absolute;width:194px;height:146px;background:#fff;overflow:hidden;box-shadow:0 0 2px rgba(0,0,0,.35)}
.num{position:absolute;font:700 7.5px 'Open Sans',sans-serif;color:#222}
.abs{position:absolute}
.h{position:absolute;left:6px;top:5px;width:140px;font:700 6.6px/1.05 'Roboto Condensed',sans-serif;color:var(--navy)}
.brand{position:absolute;right:6px;top:4px;font:400 8px 'Open Sans',sans-serif;color:#264e73}
.rule{position:absolute;left:6px;right:6px;top:16px;height:.6px;background:var(--blue)}
.foot{position:absolute;left:6px;right:6px;bottom:4px;border-top:.6px solid var(--blue);padding-top:1px;font-size:3px;color:var(--soft);display:flex;justify-content:space-between}
.foot b{font-weight:700;color:var(--navy);font-size:3.4px}
.t{position:absolute;font-size:3.6px;line-height:1.45;color:var(--ink)}
.t p{white-space:nowrap}
.t .sub{padding-left:5px;color:#666}
.t .sub2{padding-left:10px;color:#777}
.hero{position:absolute;left:0;top:0;width:194px;height:56px;background:linear-gradient(180deg,#27b9ca,#30c3d3)}
.cover-sub{font-size:4.6px;color:#555}
.cover-tiny{font-size:3.4px;color:#777;font-style:italic}
.agenda-title{font:600 9px 'Open Sans',sans-serif}
.ag{position:absolute;font-size:4px;line-height:1}
.ag .row{display:flex;align-items:center;gap:4px;height:9px}
.ag .dot{width:6px;height:6px;border-radius:50%;background:var(--blue);color:#fff;font-size:2.8px;display:flex;align-items:center;justify-content:center}
.ag .s{padding-left:18px;height:5.6px;display:flex;align-items:center;font-size:3.3px}
.box{position:absolute;font-size:3.2px;display:flex;align-items:center;justify-content:center;text-align:center;color:#fff;border-radius:1.5px;line-height:1.2}
.col{position:absolute;font-size:2.8px;line-height:1.4;color:#333}
.tbl{position:absolute;border-collapse:collapse;font-size:3px}
.tbl td{padding:.6px 2px;border-bottom:.4px solid #ccc}
.tbl .th td{background:var(--blue);color:#fff;font-weight:700}
</style>
</head>
<body>
<div class="page-title">PPT DESIGN IDEA- PART 1</div>
<div class="board">

<!-- Row 1 -->
<div class="slide" style="left:6px;top:6px">
  <div class="hero" role="img" aria-label="Illustration of darts and an arrow on a teal sky"></div>
  <svg class="abs" style="left:0;top:60px" width="118" height="18"><polygon points="0,0 108,0 116,9 108,18 0,18" fill="#3a8fd8"/></svg>
  <div class="abs" style="left:3px;top:63px;font:600 8.6px 'Open Sans',sans-serif;color:#fff">Sorrel Growth Equity</div>
  <div class="abs cover-sub" style="left:40px;top:94px">Introduction to Team and Track Record</div>
  <div class="abs cover-tiny" style="left:40px;top:102px">For US Investors<br>November 2016</div>
  <div class="abs" style="right:4px;bottom:4px;font:600 6px 'Open Sans',sans-serif;color:#264e73">Sorrel Growth Equity</div>
</div>
<div class="num" style="left:190px;top:154px">0</div>

<div class="slide" style="left:243px;top:6px">
  <div class="hero" role="img" aria-label="Illustration of darts and an arrow on a teal sky"></div>
  <div class="abs" style="left:0;width:194px;top:66px;text-align:center;font:600 10.5px 'Open Sans',sans-serif;color:#333">Sorrel Growth Equity</div>
  <div class="abs cover-sub" style="left:0;width:194px;top:82px;text-align:center">Introduction to Team and Track Record</div>
  <div class="abs cover-tiny" style="left:0;width:194px;top:92px;text-align:center">For US Investors<br>November 2016</div>
  <div class="brand" style="top:118px;right:0;left:0;text-align:center;font-size:10px">Brannock</div>
</div>
<div class="num" style="left:427px;top:154px">1</div>

<div class="slide" style="left:480px;top:6px">
  <div class="hero" role="img" aria-label="Illustration of darts and an arrow on a teal sky"></div>
  <svg class="abs" style="left:18px;top:62px" width="160" height="26"><polygon points="0,14 8,14 8,26 0,20" fill="#2a9a9a"/><polygon points="160,14 152,14 152,26 160,20" fill="#2a9a9a"/><rect x="6" y="0" width="148" height="16" fill="#2f86c9"/><rect x="12" y="16" width="136" height="9" fill="#fff"/></svg>
  <div class="abs" style="left:0;width:194px;top:64px;text-align:center;font:700 9px 'Roboto Condensed',sans-serif;color:#fff">SORREL GROWTH EQUITY</div>
  <div class="abs cover-sub" style="left:0;width:194px;top:79px;text-align:center">Introduction to Team and Track Record</div>
  <div class="abs cover-tiny" style="left:0;width:194px;top:91px;text-align:center">For US Investors<br>November 2016</div>
  <div class="brand" style="top:118px;right:10px;font-size:10px">Brannock</div>
</div>
<div class="num" style="left:664px;top:154px">2</div>

<div class="slide" style="left:716px;top:6px">
  <div class="abs" style="left:0;top:0;width:194px;height:54px;background:var(--blue)"></div>
  <div class="abs" style="left:0;width:194px;top:20px;text-align:center;font:600 10.5px 'Open Sans',sans-serif;color:#fff">Sorrel Growth Equity</div>
  <div class="abs cover-sub" style="left:0;width:194px;top:72px;text-align:center">Introduction to Team and Track Record</div>
  <div class="abs cover-tiny" style="left:0;width:194px;top:81px;text-align:center">For US Investors<br>November 2016</div>
  <div class="brand" style="top:122px;right:10px;font-size:10px">Brannock</div>
</div>
<div class="num" style="left:900px;top:154px">3</div>

<div class="slide" style="left:953px;top:6px">
  <svg class="abs" style="left:0;top:0" width="194" height="146"><polygon points="140,0 194,0 194,146 120,146 160,73" fill="var(--blue)"/><rect x="0" y="138" width="194" height="8" fill="var(--blue)"/></svg>
  <div class="abs agenda-title" style="left:14px;top:10px;color:var(--blue)">Agenda</div>
  <div class="t" style="left:26px;top:26px">
    <p>› Executive Summary</p><p>› Differentiated Model</p>
    <p class="sub">• Team and Advisory Board</p><p class="sub">• Target Profile</p><p class="sub">• Proprietary Company and Executive Sourcing</p><p class="sub">• Operational Focus</p>
    <p>› Track Record</p><p>› Summary of Terms</p><p>› Appendix</p>
  </div>
  <div class="brand" style="top:126px;left:4px;right:auto;font-size:10px">Brannock</div>
</div>
<div class="num" style="left:1137px;top:154px">4</div>

<!-- Row 2 -->
<div class="slide" style="left:6px;top:174px">
  <div class="abs" role="img" aria-label="Soft blurred blue-grey background photo" style="left:0;top:0;width:64px;height:146px;background:linear-gradient(180deg,#6f8796,#465c6b 60%,#3a4e5c)"></div>
  <div class="abs agenda-title" style="left:14px;top:8px;color:#fff">Agenda</div>
  <div class="brand" style="top:8px;font-size:10px">Brannock</div>
  <div class="ag" style="left:62px;top:33px">
    <div class="row"><span class="dot">01</span>Executive Summary</div>
    <div class="row"><span class="dot">02</span>Differentiated Model</div>
    <div class="s">• Team and Advisory Board</div><div class="s">• Target Profile</div><div class="s">• Proprietary Company and Executive Sourcing</div><div class="s">• Operational Focus</div>
    <div class="row"><span class="dot">03</span>Track Record</div>
    <div class="row"><span class="dot">04</span>Summary of Terms</div>
    <div class="row"><span class="dot">05</span>Appendix</div>
  </div>
</div>
<div class="num" style="left:190px;top:322px">5</div>

<div class="slide" style="left:243px;top:174px;background:#fff">
  <svg class="abs" style="left:0;top:0" width="194" height="146"><polygon points="0,0 130,0 194,110 194,146 0,146" fill="var(--blue)"/><polygon points="130,0 194,0 194,110" fill="#fff"/><polygon points="150,146 194,70 194,146" fill="#5cbde5"/></svg>
  <div class="abs agenda-title" style="left:14px;top:6px;color:#fff">Agenda</div>
  <div class="brand" style="top:8px;font-size:10px">Brannock</div>
  <div class="ag" style="left:24px;top:33px;color:#fff">
    <div class="row"><span class="dot" style="background:#1d5ea8">01</span>Executive Summary</div>
    <div class="row"><span class="dot" style="background:#1d5ea8">02</span>Differentiated Model</div>
    <div class="s">• Team and Advisory Board</div><div class="s">• Target Profile</div><div class="s">• Proprietary Company and Executive Sourcing</div><div class="s">• Operational Focus</div>
    <div class="row"><span class="dot" style="background:#1d5ea8">03</span>Track Record</div>
    <div class="row"><span class="dot" style="background:#1d5ea8">04</span>Summary of Terms</div>
    <div class="row"><span class="dot" style="background:#1d5ea8">05</span>Appendix</div>
  </div>
</div>
<div class="num" style="left:427px;top:322px">6</div>

<div class="slide" style="left:480px;top:174px">
  <svg class="abs" style="left:0;top:0" width="194" height="146"><polygon points="130,146 194,60 194,146" fill="var(--blue)"/></svg>
  <div class="abs agenda-title" style="left:14px;top:6px;color:#444">Agenda</div>
  <div class="brand" style="top:8px;font-size:10px">Brannock</div>
  <div class="rule" style="top:20px;background:#ddd"></div>
  <div class="ag" style="left:20px;top:33px">
    <div class="row"><span class="dot">01</span>Executive Summary</div>
    <div class="row"><span class="dot">02</span>Differentiated Model</div>
    <div class="s">• Team and Advisory Board</div><div class="s">• Target Profile</div><div class="s">• Proprietary Company and Executive Sourcing</div><div class="s">• Operational Focus</div>
    <div class="row"><span class="dot">03</span>Track Record</div>
    <div class="row"><span class="dot">04</span>Summary of Terms</div>
    <div class="row"><span class="dot">05</span>Appendix</div>
  </div>
</div>
<div class="num" style="left:664px;top:322px">7</div>

<div class="slide" style="left:716px;top:174px">
  <svg class="abs" style="left:0;top:0" width="194" height="146"><polygon points="130,0 194,0 194,146 100,146 168,73" fill="var(--blue)"/><rect x="0" y="138" width="194" height="8" fill="var(--blue)"/></svg>
  <div class="t" style="left:32px;top:30px;font-size:4.4px">
    <p style="color:#333">› Executive Summary</p><p style="color:#aaa">› Differentiated Model</p>
    <p class="sub" style="color:#bbb">• Team and Advisory Board</p><p class="sub" style="color:#bbb">• Target Profile</p><p class="sub" style="color:#bbb">• Proprietary Company and Executive Sourcing</p><p class="sub" style="color:#bbb">• Operational Focus</p>
    <p style="color:#aaa">› Track Record</p><p style="color:#aaa">› Summary of Terms</p><p style="color:#aaa">› Appendix</p>
  </div>
  <div class="brand" style="top:126px;left:4px;right:auto;font-size:10px">Brannock</div>
</div>
<div class="num" style="left:900px;top:322px">8</div>

<div class="slide" style="left:953px;top:174px">
  <div class="h">Sorrel Growth Equity Overview</div><div class="brand">Brannock</div><div class="rule"></div>
  <div class="t" style="left:10px;top:28px;font-size:3.2px">
    <p>› Ascend</p><p>› Ascend</p><p class="sub">• 30+ years of work history / 12 years in growth</p><p class="sub">  equity investing</p><p class="sub">• Successful track record</p><p class="sub">• Proven, differentiated sourcing and investment model</p>
    <p style="margin-top:3px">› Focused on high growth buyout opportunities in North</p><p>  America</p><p style="margin-top:3px">› New management company and carry ownership held</p><p>  exclusively by the US team and advisors</p>
  </div>
  <div class="abs" role="img" aria-label="Illustration of a lightbulb with gears" style="left:158px;top:40px;width:30px;height:42px;border-radius:50% 50% 30% 30%;background:radial-gradient(circle at 50% 40%,#8fd0ee,#2f86c9)"></div>
  <div class="foot"><span>Confidential 9</span><b>Sorrel Growth Equity</b></div>
</div>
<div class="num" style="left:1137px;top:322px">9</div>

<!-- Row 3 -->
<div class="slide" style="left:6px;top:342px">
  <div class="h">Executive Summary</div><div class="brand">Brannock</div><div class="rule"></div>
  <div class="t" style="left:8px;top:22px;font-size:3px">
    <p>› Over a Decade of Superior Value Creation</p><p class="sub">• 1</p><p class="sub">• 2</p>
    <p>› Achieving Superior Returns</p><p class="sub">• 1</p><p class="sub">• 2</p>
    <p>› Repeatable Sourcing Model</p><p class="sub">• Disciplined investment focus targeting companies with</p><p class="sub2">• Revenues of $5M to $50M with growth of 20% to 100%</p><p class="sub2">• First institutional capital, efficient businesses</p><p class="sub2">• Enterprise values of $15M to $75M, returns of $30M+</p><p class="sub2">• Control transactions and growth equity</p><p class="sub">• Proprietary predictive model for company sourcing</p>
    <p>› Building Successful Businesses</p><p class="sub">• Proven, capital efficient CEO and founder partnerships</p><p class="sub">• Work closely with teams to create value</p>
  </div>
  <div class="abs" role="img" aria-label="Illustration of a target with an arrow in the bullseye" style="left:150px;top:30px;width:36px;height:36px;border-radius:50%;background:radial-gradient(circle,#f5b820 0 22%,#fff 23% 40%,#33a6d7 41%)"></div>
  <div class="foot"><span>Confidential 10</span><b>Sorrel Growth Equity</b></div>
</div>
<div class="num" style="left:186px;top:490px">10</div>

<div class="slide" style="left:243px;top:342px">
  <div class="h">Achieving Superior Revenue</div><div class="brand">Brannock</div><div class="rule"></div>
  <div class="t" style="left:8px;top:20px;font-size:3px"><p>› US High Growth Buyout/Equity Portfolio 2004 through June 2016</p><p class="sub" style="color:#999">(Adjusted for investments announced June 2016)</p>
  <p class="sub" style="margin-top:3px">• 1</p><p class="sub">• 2</p><p class="sub">• 3</p><p class="sub">• 4</p><p class="sub">• 5</p><p class="sub">• 6</p><p class="sub">• 7</p><p class="sub">• 8</p></div>
  <div class="abs" style="left:112px;top:34px;width:74px;height:52px;background:#f0f0f0"></div>
  <div class="abs" style="left:112px;top:36px;width:74px;text-align:center;font-size:3px;font-weight:700">US Growth Returns</div>
  <svg class="abs" style="left:112px;top:44px" width="74" height="42"><g stroke="#ddd" stroke-width=".4"><line x1="6" y1="8" x2="70" y2="8"/><line x1="6" y1="16" x2="70" y2="16"/><line x1="6" y1="24" x2="70" y2="24"/><line x1="6" y1="32" x2="70" y2="32"/></g><rect x="14" y="22" width="12" height="14" fill="var(--sea)"/><rect x="46" y="12" width="12" height="24" fill="var(--sea)"/><line x1="26" y1="22" x2="46" y2="12" stroke="#999" stroke-width=".4" stroke-dasharray="1,1"/></svg>
  <div class="t" style="left:8px;top:110px;font-size:2.4px;color:#777"><p>• Notes on returns are net of fees for the full investment period across all funds</p><p>• Past performance is not an indicator of future returns for investors</p><p>• Portfolio figures include realized and unrealized investments</p></div>
  <div class="foot"><span>Confidential 11</span><b>Sorrel Growth Equity</b></div>
</div>
<div class="num" style="left:423px;top:490px">11</div>

<div class="slide" style="left:480px;top:342px">
  <div class="h">Achieving Superior Returns</div><div class="brand">Brannock</div><div class="rule"></div>
  <div class="t" style="left:8px;top:20px;font-size:3px"><p>› US High Growth Buyout/Equity Portfolio 2004 through June 2016</p><p class="sub" style="color:#999">(Adjusted for investments announced June 2016)</p>
  <p class="sub" style="margin-top:3px">• 1</p><p class="sub">• 2</p><p class="sub">• 3</p><p class="sub">• 4</p><p class="sub">• 5</p><p class="sub">• 6</p><p class="sub">• 7</p><p class="sub">• 8</p></div>
  <div class="abs" style="left:112px;top:34px;width:74px;height:52px;background:#f0f0f0"></div>
  <div class="abs" style="left:112px;top:36px;width:74px;text-align:center;font-size:3px;font-weight:700">US Growth Returns</div>
  <svg class="abs" style="left:112px;top:44px" width="74" height="42"><g stroke="#ddd" stroke-width=".4"><line x1="6" y1="8" x2="70" y2="8"/><line x1="6" y1="16" x2="70" y2="16"/><line x1="6" y1="24" x2="70" y2="24"/><line x1="6" y1="32" x2="70" y2="32"/></g><rect x="14" y="22" width="12" height="14" fill="var(--sea)"/><rect x="46" y="12" width="12" height="24" fill="var(--sea)"/><line x1="26" y1="22" x2="46" y2="12" stroke="#999" stroke-width=".4" stroke-dasharray="1,1"/></svg>
  <div class="t" style="left:8px;top:110px;font-size:2.4px;color:#777"><p>• Notes on returns are net of fees for the full investment period across all funds</p><p>• Past performance is not an indicator of future returns for investors</p><p>• Portfolio figures include realized and unrealized investments</p></div>
  <div class="foot"><span>Confidential 12</span><b>Sorrel Growth Equity</b></div>
</div>
<div class="num" style="left:660px;top:490px">12</div>

<div class="slide" style="left:716px;top:342px">
  <div class="h" style="width:110px">Lower Middle Market Provides the Majority of Tech Exits…</div><div class="brand">Brannock</div><div class="rule" style="top:21px"></div>
  <div class="abs" style="left:14px;top:46px;font-size:3px;font-weight:700">M&amp;A Private Tech Companies 2005-2015</div>
  <table class="tbl" style="left:18px;top:58px;width:92px">
    <tr><td><b>Exit Range</b></td><td><b>Total Deals</b></td><td><b>%</b></td></tr>
    <tr><td>$500M+</td><td>150</td><td>8%</td></tr><tr><td>$300-500M</td><td>141</td><td>8%</td></tr><tr><td>$150-300M</td><td>272</td><td>15%</td></tr><tr><td>$50-150M</td><td>568</td><td>32%</td></tr><tr><td>$20-50M</td><td>661</td><td>37%</td></tr><tr><td><b>Total</b></td><td><b>1792</b></td><td><b>100%</b></td></tr>
  </table>
  <div class="box" style="left:140px;top:40px;width:46px;height:14px;background:#2f86c9">Larger fund size = more growth</div>
  <div class="box" style="left:140px;top:62px;width:46px;height:12px;background:#2f86c9">Nearly half of all exits</div>
  <div class="box" style="left:140px;top:80px;width:46px;height:12px;background:#2f86c9">Sorrel exit range</div>
  <div class="foot"><span>Confidential 13</span><b>Sorrel Growth Equity</b></div>
</div>
<div class="num" style="left:896px;top:490px">13</div>

<div class="slide" style="left:953px;top:342px">
  <div class="h" style="width:110px">Lower Middle Market Provides the Majority of Tech Exits…</div><div class="brand">Brannock</div><div class="rule" style="top:21px"></div>
  <table class="tbl" style="left:12px;top:48px;width:86px">
    <tr class="th"><td>Exit Range</td><td>Total Deals</td><td>%</td></tr>
    <tr><td>$500M+</td><td>150</td><td>8%</td></tr><tr><td>$300-500M</td><td>141</td><td>8%</td></tr><tr><td>$150-300M</td><td>272</td><td>15%</td></tr><tr><td>$50-150M</td><td>568</td><td>32%</td></tr><tr><td>$20-50M</td><td>661</td><td>37%</td></tr><tr><td>Total</td><td>1792</td><td>100%</td></tr>
  </table>
  <div class="box" style="left:144px;top:38px;width:42px;height:20px;background:var(--blue)">Larger fund size = more growth</div>
  <div class="box" style="left:144px;top:64px;width:42px;height:12px;background:var(--blue)">Nearly half of all exits</div>
  <div class="box" style="left:144px;top:82px;width:42px;height:14px;background:var(--blue)">Sorrel exit range</div>
  <div class="foot"><span>Confidential 14</span><b>Sorrel Growth Equity</b></div>
</div>
<div class="num" style="left:1133px;top:490px">14</div>

<!-- Row 4 -->
<div class="slide" style="left:6px;top:514px">
  <div class="h">With Strong Upside for Higher Value Outcomes</div><div class="brand">Brannock</div><div class="rule"></div>
  <div class="abs" style="left:10px;top:24px;font-size:3px;font-weight:700">M&amp;A Private Tech Companies 2005-2015</div>
  <svg class="abs" style="left:72px;top:26px" width="120" height="94"><polygon points="60,0 120,90 0,90" fill="var(--cream)"/></svg>
  <table class="tbl" style="left:8px;top:38px;width:78px;background:#fff">
    <tr class="th"><td>Exit Range</td><td>Total Deals</td><td>%</td></tr>
    <tr><td>$500M+</td><td>150</td><td>8%</td></tr><tr><td>$300-500M</td><td>141</td><td>8%</td></tr><tr><td>$150-300M</td><td>272</td><td>15%</td></tr><tr><td>$50-150M</td><td>568</td><td>32%</td></tr><tr><td>$20-50M</td><td>661</td><td>37%</td></tr>
  </table>
  <div class="t" style="left:112px;top:42px;font-size:2.8px;line-height:3.2"><p>Large buyout funds</p><p>Upper mid-market funds</p><p>Mid-market growth funds</p><p>&nbsp;</p><p>Sorrel Growth and peers</p><p>&nbsp;</p><p>Venture, Angel, Seed Funds</p></div>
  <div class="foot"><span>Confidential 15</span><b>Sorrel Growth Equity</b></div>
</div>
<div class="num" style="left:186px;top:662px">15</div>

<div class="slide" style="left:243px;top:514px">
  <div class="h" style="width:120px">Lower Middle Market Offers High Value Creation for Growth</div><div class="brand">Brannock</div><div class="rule" style="top:21px"></div>
  <svg class="abs" style="left:8px;top:26px" width="180" height="100">
    <line x1="14" y1="4" x2="14" y2="88" stroke="#666" stroke-width=".6"/><line x1="14" y1="88" x2="170" y2="88" stroke="#666" stroke-width=".6"/>
    <rect x="16" y="4" width="26" height="84" fill="#eee"/>
    <path d="M16,84 C60,82 80,70 95,40 C105,20 120,12 140,8" stroke="var(--blue)" stroke-width="1.2" fill="none"/>
    <rect x="64" y="66" width="16" height="6" fill="var(--blue)"/><rect x="72" y="48" width="14" height="6" fill="var(--blue)"/><rect x="76" y="38" width="14" height="6" fill="var(--blue)"/><rect x="82" y="28" width="14" height="6" fill="var(--blue)"/>
    <rect x="98" y="22" width="24" height="5" fill="#ccc"/><rect x="98" y="32" width="24" height="5" fill="#ccc"/><rect x="98" y="42" width="24" height="5" fill="#ccc"/><rect x="98" y="52" width="24" height="5" fill="#ccc"/>
    <rect x="142" y="14" width="28" height="60" fill="var(--mint)"/><rect x="142" y="14" width="28" height="6" fill="var(--blue)"/>
  </svg>
  <div class="t" style="left:152px;top:48px;font-size:3px;color:#2f86c9;line-height:3.6"><p>$165M</p><p>$250M/$500M</p><p>$400M</p><p>$95M</p></div>
  <div class="t" style="left:62px;top:34px;font-size:3px;color:#333;font-weight:700"><p>Exit</p><p>Revenue</p></div>
  <div class="abs" style="left:105px;top:118px;font-size:3px">Time / Stage</div>
  <div class="foot"><span>Confidential 16</span><b>Sorrel Growth Equity</b></div>
</div>
<div class="num" style="left:423px;top:662px">16</div>

<div class="slide" style="left:480px;top:514px">
  <div class="h">Differentiated Model: Four Pillars for Success</div><div class="brand">Brannock</div><div class="rule"></div>
  <div class="t" style="left:8px;top:22px;font-size:2.9px">
    <p>› Team and Advisory Board</p><p class="sub">• Team with strong investment and technology backgrounds</p><p class="sub">• Executive board recruitment from advisors</p><p class="sub">• Proven founders and CEOs with capital efficient, high value exits</p>
    <p style="margin-top:2px">› Target Profile</p><p class="sub">• Growth focused, significant minority</p><p class="sub">• Recurring revenue of $5M to $50M with growth of 20%+</p><p class="sub">• Capital efficient businesses with significant ownership by founder</p>
    <p style="margin-top:2px">› Proprietary Company / Executive Sourcing</p><p class="sub">• Algorithmic approach analyzes 100K companies every 6 weeks</p><p class="sub">• Companies screened for metrics and predicted growth</p><p class="sub">• Regional high value events with executive advisory board</p>
    <p style="margin-top:2px">› Operational Focus</p><p class="sub">• Team building and operational focus created strong gains</p><p class="sub">• Drive investment rapid team development and growth</p><p class="sub">• Price discipline on investments, target returns at exit</p>
  </div>
  <div class="foot"><span>Confidential 17</span><b>Sorrel Growth Equity</b></div>
</div>
<div class="num" style="left:660px;top:662px">17</div>

<div class="slide" style="left:716px;top:514px">
  <div class="h">Differentiated Model: Four Pillars for Success</div><div class="brand">Brannock</div><div class="rule"></div>
  <svg class="abs" style="left:10px;top:24px" width="176" height="40">
    <g><polygon points="4,8 34,8 40,2 10,2" fill="#3fa3a3"/><rect x="4" y="8" width="30" height="28" fill="#2a8f94"/><polygon points="34,8 40,2 40,30 34,36" fill="#1f7479"/></g>
    <g transform="translate(46,0)"><polygon points="4,8 34,8 40,2 10,2" fill="#e4e6c4"/><rect x="4" y="8" width="30" height="28" fill="#d3d6a8"/><polygon points="34,8 40,2 40,30 34,36" fill="#b9bc8c"/></g>
    <g transform="translate(92,0)"><polygon points="4,8 34,8 40,2 10,2" fill="#a5d6a7"/><rect x="4" y="8" width="30" height="28" fill="#7cbf83"/><polygon points="34,8 40,2 40,30 34,36" fill="#5fa567"/></g>
    <g transform="translate(138,0)"><polygon points="4,8 34,8 40,2 10,2" fill="#fde7b3"/><rect x="4" y="8" width="30" height="28" fill="#f9d98b"/><polygon points="34,8 40,2 40,30 34,36" fill="#e9c26b"/></g>
  </svg>
  <div class="box" style="left:14px;top:68px;width:30px;height:5px;background:var(--deep)">Team and Advisory Board</div>
  <div class="box" style="left:60px;top:68px;width:30px;height:5px;background:var(--deep)">Target Profile</div>
  <div class="box" style="left:106px;top:68px;width:30px;height:5px;background:var(--deep)">Proprietary Sourcing</div>
  <div class="box" style="left:152px;top:68px;width:30px;height:5px;background:var(--deep)">Operational Focus</div>
  <div class="col" style="left:14px;top:76px;width:32px">• Team with strong investment and technology skills<br>• Executive board from proven advisors<br>• Proven founders with high value exits</div>
  <div class="col" style="left:60px;top:76px;width:32px">• Growth focused, significant minority<br>• Recurring revenue of $5M to $50M<br>• Capital efficient businesses</div>
  <div class="col" style="left:106px;top:76px;width:32px">• Algorithmic approach screens 100K firms<br>• Companies ranked on growth metrics<br>• Regional high value events</div>
  <div class="col" style="left:152px;top:76px;width:32px">• Team building drives strong gains<br>• Rapid team development<br>• Price discipline on every deal</div>
  <div class="foot"><span>Confidential 18</span><b>Sorrel Growth Equity</b></div>
</div>
<div class="num" style="left:896px;top:662px">18</div>

<div class="slide" style="left:953px;top:514px">
  <div class="abs" style="left:0;top:64px;width:194px;height:82px;background:var(--mint)"></div>
  <div class="h">Differentiated Model: Four Pillars for Success</div><div class="brand">Brannock</div><div class="rule"></div>
  <svg class="abs" style="left:10px;top:24px" width="176" height="40">
    <g><polygon points="4,8 34,8 40,2 10,2" fill="#3fa3a3"/><rect x="4" y="8" width="30" height="28" fill="#2a8f94"/><polygon points="34,8 40,2 40,30 34,36" fill="#1f7479"/></g>
    <g transform="translate(46,0)"><polygon points="4,8 34,8 40,2 10,2" fill="#e4e6c4"/><rect x="4" y="8" width="30" height="28" fill="#d3d6a8"/><polygon points="34,8 40,2 40,30 34,36" fill="#b9bc8c"/></g>
    <g transform="translate(92,0)"><polygon points="4,8 34,8 40,2 10,2" fill="#a5d6a7"/><rect x="4" y="8" width="30" height="28" fill="#7cbf83"/><polygon points="34,8 40,2 40,30 34,36" fill="#5fa567"/></g>
    <g transform="translate(138,0)"><polygon points="4,8 34,8 40,2 10,2" fill="#fde7b3"/><rect x="4" y="8" width="30" height="28" fill="#f9d98b"/><polygon points="34,8 40,2 40,30 34,36" fill="#e9c26b"/></g>
  </svg>
  <div class="box" style="left:14px;top:68px;width:32px;height:54px;background:#2a8f94;align-items:flex-start;padding-top:2px">Team and Advisory Board</div>
  <div class="box" style="left:60px;top:68px;width:32px;height:54px;background:#b9bc8c;align-items:flex-start;padding-top:2px">Target Profile</div>
  <div class="box" style="left:106px;top:68px;width:32px;height:54px;background:#5fa567;align-items:flex-start;padding-top:2px">Proprietary Sourcing</div>
  <div class="box" style="left:152px;top:68px;width:32px;height:54px;background:#e9c26b;align-items:flex-start;padding-top:2px">Operational Focus</div>
  <div class="col" style="left:16px;top:80px;width:30px;color:#fff">• Strong investment skills<br>• Proven advisors<br>• High value exits</div>
  <div class="col" style="left:62px;top:80px;width:30px;color:#fff">• Growth focused<br>• $5M to $50M revenue<br>• Capital efficient</div>
  <div class="col" style="left:108px;top:80px;width:30px;color:#fff">• Screens 100K firms<br>• Ranked on growth<br>• Regional events</div>
  <div class="col" style="left:154px;top:80px;width:30px;color:#fff">• Team building<br>• Rapid development<br>• Price discipline</div>
  <div class="foot"><span>Confidential 19</span><b>Sorrel Growth Equity</b></div>
</div>
<div class="num" style="left:1133px;top:662px">19</div>

<!-- Row 5 -->
<div class="slide" style="left:6px;top:682px">
  <div class="abs" style="left:0;top:76px;width:194px;height:70px;background:var(--mint)"></div>
  <div class="h">Differentiated Model: Four Pillars for Success</div><div class="brand">Brannock</div><div class="rule"></div>
  <div class="box" style="left:14px;top:28px;width:34px;height:6px;background:#2a8f94">Team and Advisory Board</div>
  <div class="box" style="left:58px;top:28px;width:34px;height:6px;background:#2a8f94">Target Profile</div>
  <div class="box" style="left:102px;top:28px;width:34px;height:6px;background:#2a8f94">Proprietary Sourcing</div>
  <div class="box" style="left:146px;top:28px;width:34px;height:6px;background:#2a8f94">Operational Focus</div>
  <svg class="abs" style="left:14px;top:38px" width="170" height="74">
    <g fill="#2a8f94"><rect x="0" y="4" width="34" height="64"/><ellipse cx="17" cy="68" rx="17" ry="4"/><ellipse cx="17" cy="4" rx="17" ry="4" fill="#5fb5b8"/></g>
    <g fill="#2a8f94" transform="translate(44,0)"><rect x="0" y="4" width="34" height="64"/><ellipse cx="17" cy="68" rx="17" ry="4"/><ellipse cx="17" cy="4" rx="17" ry="4" fill="#5fb5b8"/></g>
    <g fill="#2a8f94" transform="translate(88,0)"><rect x="0" y="4" width="34" height="64"/><ellipse cx="17" cy="68" rx="17" ry="4"/><ellipse cx="17" cy="4" rx="17" ry="4" fill="#5fb5b8"/></g>
    <g fill="#2a8f94" transform="translate(132,0)"><rect x="0" y="4" width="34" height="64"/><ellipse cx="17" cy="68" rx="17" ry="4"/><ellipse cx="17" cy="4" rx="17" ry="4" fill="#5fb5b8"/></g>
  </svg>
  <div class="col" style="left:17px;top:48px;width:30px;color:#fff">• Strong investment skills<br>• Proven advisors<br>• High value exits</div>
  <div class="col" style="left:61px;top:48px;width:30px;color:#fff">• Growth focused<br>• $5M to $50M revenue<br>• Capital efficient</div>
  <div class="col" style="left:105px;top:48px;width:30px;color:#fff">• Screens 100K firms<br>• Ranked on growth<br>• Regional events</div>
  <div class="col" style="left:149px;top:48px;width:30px;color:#fff">• Team building<br>• Rapid development<br>• Price discipline</div>
  <div class="foot"><span>Confidential 20</span><b>Sorrel Growth Equity</b></div>
</div>
<div class="num" style="left:186px;top:830px">20</div>

<div class="slide" style="left:243px;top:682px">
  <div class="abs" style="left:0;top:76px;width:194px;height:70px;background:var(--mint)"></div>
  <div class="h">Differentiated Model: Four Pillars for Success</div><div class="brand">Brannock</div><div class="rule"></div>
  <div class="box" style="left:14px;top:28px;width:34px;height:6px;background:var(--deep)">Team and Advisory Board</div>
  <div class="box" style="left:58px;top:28px;width:34px;height:6px;background:var(--deep)">Target Profile</div>
  <div class="box" style="left:102px;top:28px;width:34px;height:6px;background:var(--deep)">Proprietary Sourcing</div>
  <div class="box" style="left:146px;top:28px;width:34px;height:6px;background:var(--deep)">Operational Focus</div>
  <svg class="abs" style="left:14px;top:38px" width="170" height="74">
    <g fill="#2a8f94"><rect x="0" y="4" width="34" height="64"/><ellipse cx="17" cy="68" rx="17" ry="4"/><ellipse cx="17" cy="4" rx="17" ry="4" fill="#5fb5b8"/></g>
    <g fill="#c9cc9c" transform="translate(44,0)"><rect x="0" y="4" width="34" height="64"/><ellipse cx="17" cy="68" rx="17" ry="4"/><ellipse cx="17" cy="4" rx="17" ry="4" fill="#e4e6c4"/></g>
    <g fill="#7cbf83" transform="translate(88,0)"><rect x="0" y="4" width="34" height="64"/><ellipse cx="17" cy="68" rx="17" ry="4"/><ellipse cx="17" cy="4" rx="17" ry="4" fill="#a5d6a7"/></g>
    <g fill="#e9c26b" transform="translate(132,0)"><rect x="0" y="4" width="34" height="64"/><ellipse cx="17" cy="68" rx="17" ry="4"/><ellipse cx="17" cy="4" rx="17" ry="4" fill="#fde7b3"/></g>
  </svg>
  <div class="col" style="left:17px;top:48px;width:30px;color:#fff">• Strong investment skills<br>• Proven advisors<br>• High value exits</div>
  <div class="col" style="left:61px;top:48px;width:30px">• Growth focused<br>• $5M to $50M revenue<br>• Capital efficient</div>
  <div class="col" style="left:105px;top:48px;width:30px">• Screens 100K firms<br>• Ranked on growth<br>• Regional events</div>
  <div class="col" style="left:149px;top:48px;width:30px">• Team building<br>• Rapid development<br>• Price discipline</div>
  <div class="foot"><span>Confidential 21</span><b>Sorrel Growth Equity</b></div>
</div>
<div class="num" style="left:423px;top:830px">21</div>

<div class="slide" style="left:480px;top:682px">
  <svg class="abs" style="left:0;top:0" width="194" height="146"><polygon points="130,0 194,0 194,146 100,146 150,73" fill="var(--blue)"/><polygon points="150,73 194,0 194,146" fill="#2f86c9"/><rect x="0" y="138" width="194" height="8" fill="var(--blue)"/></svg>
  <div class="t" style="left:32px;top:28px;font-size:4.2px">
    <p style="color:#aaa">› Executive Summary</p><p style="color:#333">› Differentiated Model</p>
    <p class="sub">• Team and Advisory Board</p><p class="sub">• Target Profile</p><p class="sub">• Proprietary Company and Executive Sourcing</p><p class="sub">• Operational Focus</p>
    <p style="color:#aaa">› Track Record</p><p style="color:#aaa">› Summary of Terms</p><p style="color:#aaa">› Appendix</p>
  </div>
  <div class="brand" style="top:126px;left:4px;right:auto;font-size:10px">Brannock</div>
</div>
<div class="num" style="left:660px;top:830px">22</div>

<div class="slide" style="left:716px;top:682px">
  <div class="h">Differentiated Model: Four Pillars for Success</div><div class="brand">Brannock</div><div class="rule"></div>
  <svg class="abs" style="left:47px;top:22px" width="100" height="100" viewBox="0 0 100 100">
    <circle cx="50" cy="50" r="34" fill="none" stroke="var(--deep)" stroke-width="28"/>
    <circle cx="50" cy="50" r="20" fill="#fff"/>
    <g stroke="#fff" stroke-width="1.4"><line x1="50" y1="2" x2="50" y2="30"/><line x1="98" y1="50" x2="70" y2="50"/><line x1="50" y1="98" x2="50" y2="70"/><line x1="2" y1="50" x2="30" y2="50"/></g>
  </svg>
  <div class="t" style="left:66px;top:34px;font-size:3px;color:#fff;text-align:center"><p>Team and</p><p>Advisory</p><p>Board</p></div>
  <div class="t" style="left:108px;top:38px;font-size:3px;color:#fff"><p>Target</p><p>Profile</p></div>
  <div class="t" style="left:104px;top:78px;font-size:3px;color:#fff"><p>Proprietary</p><p>Company</p><p>Sourcing</p></div>
  <div class="t" style="left:62px;top:80px;font-size:3px;color:#fff"><p>Operational</p><p>Focus</p></div>
  <div class="foot"><span>Confidential 23</span><b>Sorrel Growth Equity</b></div>
</div>
<div class="num" style="left:896px;top:830px">23</div>

<div class="slide" style="left:953px;top:682px">
  <div class="h">Differentiated Model: Four Pillars for Success</div><div class="brand">Brannock</div><div class="rule"></div>
  <svg class="abs" style="left:52px;top:24px" width="90" height="90" viewBox="0 0 90 90">
    <path d="M45,45 L45,2 A43,43 0 0 0 2,45 Z" fill="var(--cream)"/>
    <path d="M45,45 L45,2 A43,43 0 0 1 88,45 Z" fill="var(--sky)"/>
    <path d="M45,45 L88,45 A43,43 0 0 1 45,88 Z" fill="var(--blue)"/>
    <path d="M45,45 L45,88 A43,43 0 0 1 2,45 Z" fill="var(--sea)"/>
    <circle cx="45" cy="45" r="18" fill="#fff"/>
  </svg>
  <div class="t" style="left:82px;top:60px;font-size:3.4px;text-align:center"><p>Four Pillars</p><p>For</p><p>Success</p></div>
  <div class="t" style="left:66px;top:38px;font-size:3px"><p>Team and</p><p>Advisory Board</p></div>
  <div class="t" style="left:120px;top:40px;font-size:3px"><p>Target</p><p>Profile</p></div>
  <div class="t" style="left:114px;top:82px;font-size:3px;color:#fff"><p>Proprietary</p><p>Sourcing</p></div>
  <div class="t" style="left:62px;top:82px;font-size:3px"><p>Operational</p><p>Focus</p></div>
  <div class="foot"><span>Confidential 24</span><b>Sorrel Growth Equity</b></div>
</div>
<div class="num" style="left:1133px;top:830px">24</div>

<!-- Row 6 -->
<div class="slide" style="left:6px;top:850px">
  <div class="h">Differentiated Model: Four Pillars for Success</div><div class="brand">Brannock</div><div class="rule"></div>
  <svg class="abs" style="left:64px;top:34px" width="66" height="66" viewBox="0 0 66 66">
    <path d="M0,0 H22 L33,20 L22,33 H0 Z" fill="var(--sea)" opacity=".85"/>
    <path d="M66,0 H44 L33,20 L44,33 H66 Z" fill="var(--cream)"/>
    <path d="M0,66 H22 L33,46 L22,33 H0 Z" fill="var(--deep)"/>
    <path d="M66,66 H44 L33,46 L44,33 H66 Z" fill="var(--sea)"/>
    <circle cx="33" cy="33" r="11" fill="#fff"/>
  </svg>
  <div class="box" style="left:14px;top:40px;width:44px;height:10px;background:var(--mint);color:#333">Team and Advisory Board</div>
  <div class="box" style="left:136px;top:40px;width:44px;height:10px;background:var(--cream);color:#333">Target Profile</div>
  <div class="box" style="left:14px;top:80px;width:44px;height:10px;background:var(--deep)">Operational Focus</div>
  <div class="box" style="left:136px;top:80px;width:44px;height:10px;background:var(--sea);color:#333">Proprietary Company / Executive Sourcing</div>
  <div class="t" style="left:87px;top:60px;width:20px;font-size:3px;text-align:center"><p>Four Pillars</p><p>For</p><p>Success</p></div>
  <div class="foot"><span>Confidential 25</span><b>Sorrel Growth Equity</b></div>
</div>
<div class="num" style="left:186px;top:998px">25</div>

<div class="slide" style="left:243px;top:850px">
  <div class="h">Differentiated Model: Four Pillars for Success</div><div class="brand">Brannock</div><div class="rule"></div>
  <svg class="abs" style="left:75px;top:46px" width="44" height="44" viewBox="0 0 44 44">
    <circle cx="22" cy="22" r="16" fill="none" stroke-width="10" stroke="var(--blue)" stroke-dasharray="24 1.2 24 1.2 24 1.2 24 1.2" transform="rotate(-90 22 22)"/>
    <circle cx="22" cy="22" r="16" fill="none" stroke-width="10" stroke="var(--gold)" stroke-dasharray="0 25.2 24 100" transform="rotate(-90 22 22)"/>
    <circle cx="22" cy="22" r="16" fill="none" stroke-width="10" stroke="#c62c2c" stroke-dasharray="0 50.4 24 100" transform="rotate(-90 22 22)"/>
    <circle cx="22" cy="22" r="16" fill="none" stroke-width="10" stroke="var(--dark)" stroke-dasharray="0 75.6 24 100" transform="rotate(-90 22 22)"/>
  </svg>
  <div class="t" style="left:87px;top:61px;width:20px;font-size:2.6px;text-align:center"><p>Four Pillars</p><p>For</p><p>Success</p></div>
  <div class="box" style="left:14px;top:44px;width:44px;height:10px;background:var(--blue)">Team and Advisory Board</div>
  <div class="box" style="left:136px;top:44px;width:44px;height:10px;background:var(--gold)">Target Profile</div>
  <div class="box" style="left:14px;top:86px;width:44px;height:10px;background:var(--dark)">Operational Focus</div>
  <div class="box" style="left:136px;top:86px;width:44px;height:10px;background:#2363a6">Proprietary Company / Executive Sourcing</div>
  <div class="foot"><span>Confidential 26</span><b>Sorrel Growth Equity</b></div>
</div>
<div class="num" style="left:423px;top:998px">26</div>

<div class="slide" style="left:480px;top:850px">
  <div class="h">Differentiated Model: Four Pillars for Success</div><div class="brand">Brannock</div><div class="rule"></div>
  <svg class="abs" style="left:75px;top:44px" width="44" height="44" viewBox="0 0 44 44">
    <circle cx="22" cy="22" r="16" fill="none" stroke-width="10" stroke="var(--sea)" stroke-dasharray="24 1.2 24 1.2 24 1.2 24 1.2" transform="rotate(-90 22 22)"/>
    <circle cx="22" cy="22" r="16" fill="none" stroke-width="10" stroke="var(--sky)" stroke-dasharray="0 25.2 24 100" transform="rotate(-90 22 22)"/>
    <circle cx="22" cy="22" r="16" fill="none" stroke-width="10" stroke="var(--mint)" stroke-dasharray="0 50.4 24 100" transform="rotate(-90 22 22)"/>
    <circle cx="22" cy="22" r="16" fill="none" stroke-width="10" stroke="var(--blue)" stroke-dasharray="0 75.6 24 100" transform="rotate(-90 22 22)"/>
  </svg>
  <div class="t" style="left:87px;top:59px;width:20px;font-size:2.6px;text-align:center"><p>Four Pillars</p><p>For</p><p>Success</p></div>
  <div class="box" style="left:14px;top:44px;width:44px;height:10px;background:var(--sea);color:#333">Team and Advisory Board</div>
  <div class="box" style="left:136px;top:44px;width:44px;height:10px;background:var(--sky);color:#333">Target Profile</div>
  <div class="box" style="left:14px;top:86px;width:44px;height:10px;background:var(--blue)">Operational Focus</div>
  <div class="box" style="left:136px;top:86px;width:44px;height:10px;background:var(--mint);color:#333">Proprietary Company / Executive Sourcing</div>
  <div class="foot"><span>Confidential 27</span><b>Sorrel Growth Equity</b></div>
</div>
<div class="num" style="left:660px;top:998px">27</div>

<div class="slide" style="left:716px;top:850px">
  <div class="h">Differentiated Model: Four Pillars for Success</div><div class="brand">Brannock</div><div class="rule"></div>
  <svg class="abs" style="left:77px;top:46px" width="40" height="40" viewBox="0 0 40 40">
    <circle cx="20" cy="20" r="16" fill="none" stroke-width="4" stroke="#3e7a53" stroke-dasharray="24 1.2 24 1.2 24 1.2 24 1.2" transform="rotate(-90 20 20)"/>
    <circle cx="20" cy="20" r="16" fill="none" stroke-width="4" stroke="#20b5b0" stroke-dasharray="0 25.2 24 100" transform="rotate(-90 20 20)"/>
    <circle cx="20" cy="20" r="16" fill="none" stroke-width="4" stroke="var(--gold)" stroke-dasharray="0 50.4 24 100" transform="rotate(-90 20 20)"/>
    <circle cx="20" cy="20" r="16" fill="none" stroke-width="4" stroke="var(--green)" stroke-dasharray="0 75.6 24 100" transform="rotate(-90 20 20)"/>
  </svg>
  <div class="t" style="left:87px;top:59px;width:20px;font-size:3px;text-align:center"><p>Four Pillars</p><p>For</p><p>Success</p></div>
  <div class="box" style="left:14px;top:44px;width:44px;height:10px;background:#3e7a53;border-radius:5px">Team and Advisory Board</div>
  <div class="box" style="left:136px;top:44px;width:44px;height:10px;background:#20b5b0;border-radius:5px">Target Profile</div>
  <div class="box" style="left:14px;top:86px;width:44px;height:10px;background:var(--green);border-radius:5px">Operational Focus</div>
  <div class="box" style="left:136px;top:86px;width:44px;height:10px;background:var(--gold);border-radius:5px">Proprietary Company / Executive Sourcing</div>
  <div class="foot"><span>Confidential 28</span><b>Sorrel Growth Equity</b></div>
</div>
<div class="num" style="left:896px;top:998px">28</div>

<div class="slide" style="left:953px;top:850px">
  <div class="h">Differentiated Model: Four Pillars for Success</div><div class="brand">Brannock</div><div class="rule"></div>
  <svg class="abs" style="left:77px;top:46px" width="40" height="40" viewBox="0 0 40 40">
    <circle cx="20" cy="20" r="16" fill="none" stroke-width="4" stroke="var(--sea)" stroke-dasharray="24 1.2 24 1.2 24 1.2 24 1.2" transform="rotate(-90 20 20)"/>
    <circle cx="20" cy="20" r="16" fill="none" stroke-width="4" stroke="var(--sky)" stroke-dasharray="0 25.2 24 100" transform="rotate(-90 20 20)"/>
    <circle cx="20" cy="20" r="16" fill="none" stroke-width="4" stroke="var(--blue)" stroke-dasharray="0 50.4 24 100" transform="rotate(-90 20 20)"/>
    <circle cx="20" cy="20" r="16" fill="none" stroke-width="4" stroke="#f3d98f" stroke-dasharray="0 75.6 24 100" transform="rotate(-90 20 20)"/>
  </svg>
  <div class="t" style="left:87px;top:59px;width:20px;font-size:3px;text-align:center"><p>Four Pillars</p><p>For</p><p>Success</p></div>
  <div class="box" style="left:14px;top:44px;width:44px;height:10px;background:var(--sea);color:#333;border-radius:5px">Team and Advisory Board</div>
  <div class="box" style="left:136px;top:44px;width:44px;height:10px;background:var(--sky);color:#333;border-radius:5px">Target Profile</div>
  <div class="box" style="left:14px;top:86px;width:44px;height:10px;background:var(--cream);color:#333;border-radius:5px">Operational Focus</div>
  <div class="box" style="left:136px;top:86px;width:44px;height:10px;background:var(--blue);border-radius:5px">Proprietary Company / Executive Sourcing</div>
  <div class="foot"><span>Confidential 29</span><b>Sorrel Growth Equity</b></div>
</div>
<div class="num" style="left:1133px;top:998px">29</div>

</div>
</body>
</html>
```